Hardcore nerd needs to stand out in a sea of dull Defence business cards

Wombat Devices is a new Australian consulting engineering company that turns research and theory into practical systems. No evangelistic fluff, just mathematics and physics into electronic and optical circuits for consumer products, scientific research or Defence applications.

We already have a recognised logo (provided) which is often dark blue/black on a light background but we're open to other combinations. (Us engineers tend to have limited aesthetic imagination :)

Some of our recent products have included:
* Instrumentation for electrical testing,
* Radar jammers,
* GPS antenna design,
* Satellite tracking systems,
* High power lasers

We're open to both single and double-sided designs - happy to be convinced either way.

P.S. Another group is working on the web page, so - alas - our web site is currently of no use for images/ideas...

Target Market(s)

Engineering managers,
Scientists

Contact Information for Business Card

Dr Colin Marsh
R&D Engineer

colin@wombatdevicesco.com.au
0427 563 210

PO Box XXX (to be confirmed)
Banks ACT 2913
Australia

Font styles to use
Serif
Sans Serif

Colors

Designer to choose colors to be used in the design.

Requirements
Must have
• My contact details!
• I've had many (great) "bold and plain" designs submitted already, so feel free to be artistically creative :)
• Happy to take advice re fonts/colours/printability etc.
Nice to have
• I'm not sure if "lists" are more at home on a CV than a business card, but representative services include:
• Applied electromagnetics
• RF and high speed electronics
• Signal and image processing
• Electro-optical and laser systems
• Concept-to-prototype design services
• If you're considering double sided cards, then often measuring/alignment grids/rulers feature on the back of similar cards.
• e.g. https://www.lumoptix-example.com/newgrouppage9.cfm?objectgroup_id=4815
• https://www.lumoptix-example.com/newgrouppage9.cfm?objectgroup_ID=4817
• ..or even a "Smith chart" (google will return lots)
• Generic images to represent a capability might work - googling images associated with keyword for each of these areas might help:
• - "passive radar", "phased array", "fdtd", "vircator"
• RF and high speed electronic design
• - "smith chart", "microstrip circuits", "dimensioned drawing", "electronic schematic"
• - "dft", "iir filter"
• - "optical cavity". "laser energy level diagram"
• Background/watermarked images outlines/wireframes/schematics would probably look OK.
Should not have
• If a list of projects/services is provided, it is important not to make the client feel that this is "all" the company can do. Engineering design is a creative discipline (like graphics :)
• Please, no stock "military" snaps like planes, missiles, etc!

```html
<!DOCTYPE html>
<html lang="en">
<head>
<meta charset="utf-8">
<title>Wombat Devices — Business Card</title>
<link rel="stylesheet" href="https://fonts.googleapis.com/css2?family=Montserrat:wght@300;400;700&family=Source+Sans+3:wght@700&display=swap">
<style>
  :root {
    --backdrop: #adadad;
    --card: #282828;
    --ink: #ffffff;
    --mark-faint: #4a4a4a;
  }
  * { margin: 0; padding: 0; box-sizing: border-box; }
  html, body { width: 1200px; height: 891px; overflow: hidden; }
  body {
    position: relative;
    background: var(--backdrop);
    font-family: "Montserrat", Arial, sans-serif;
    color: var(--ink);
  }
  .card {
    position: absolute;
    width: 571px;
    height: 370px;
    background: var(--card);
  }
  .card--front { left: 114px; top: 87px; }
  .card--back  { left: 516px; top: 434px; }

  /* Front: brand name */
  .brand { position: absolute; left: 119px; top: 125px; display: flex; align-items: center; gap: 10px; }
  .brand__dot { width: 116px; height: 116px; border-radius: 50%; background: var(--ink); }
  .brand__name {
    font-family: "Source Sans 3", Arial, sans-serif;
    font-weight: 700;
    color: var(--ink);
    line-height: 1;
  }
  .brand__line1 { display: block; font-size: 40px; letter-spacing: 0.5px; }
  .brand__line2 { display: block; font-size: 22px; letter-spacing: 4.6px; margin-top: 4px; }

  /* Back: contact block */
  .contact { position: absolute; left: 45px; top: 92px; }
  .contact__name { font-size: 26px; font-weight: 700; line-height: 1.2; }
  .contact__role { font-size: 19px; font-weight: 700; line-height: 1.3; }
  .contact__rule { width: 4px; height: 19px; background: var(--ink); margin: 12px 0 14px 2px; }
  .contact__lines { font-size: 19px; font-weight: 300; line-height: 22px; letter-spacing: 0.2px; }
  .contact__lines + .contact__lines { margin-top: 12px; }

  .mark-faint {
    position: absolute; left: 440px; top: 244px;
    width: 68px; height: 68px; border-radius: 50%;
    background: var(--mark-faint);
  }
  .ruler { position: absolute; right: 0; top: 0; }
</style>
</head>
<body>

<section class="card card--front">
  <div class="brand">
    <span class="brand__dot"></span>
    <span class="brand__name">
      <span class="brand__line1">WOMBAT</span>
      <span class="brand__line2">DEVICES</span>
    </span>
  </div>
</section>

<section class="card card--back">
  <div class="contact">
    <p class="contact__name">Dr Colin Marsh</p>
    <p class="contact__role">R&amp;D Engineer</p>
    <div class="contact__rule"></div>
    <p class="contact__lines">colin@wombatdevicesco.com.au<br>0427 563 210</p>
    <p class="contact__lines">PO Box XXX<br>Banks ACT 2913<br>Australia</p>
  </div>

  <span class="mark-faint"></span>

  <svg class="ruler" width="60" height="370" viewBox="511 0 60 370" aria-hidden="true">
    <path stroke="#ffffff" stroke-width="2" fill="none" d="
      M571 25h-45 M571 31.6h-20 M571 38.2h-20 M571 44.8h-20 M571 51.4h-20
      M571 58h-30 M571 64.6h-20 M571 71.2h-20 M571 77.8h-20 M571 84.4h-20
      M571 91h-45 M571 97.6h-20 M571 104.2h-20 M571 110.8h-20 M571 117.4h-20
      M571 124h-30 M571 130.6h-20 M571 137.2h-20 M571 143.8h-20 M571 150.4h-20
      M571 157h-45 M571 163.6h-20 M571 170.2h-20 M571 176.8h-20 M571 183.4h-20
      M571 190h-30 M571 196.6h-20 M571 203.2h-20 M571 209.8h-20 M571 216.4h-20
      M571 223h-45 M571 229.6h-20 M571 236.2h-20 M571 242.8h-20 M571 249.4h-20
      M571 256h-30 M571 262.6h-20 M571 269.2h-20 M571 275.8h-20 M571 282.4h-20
      M571 289h-45 M571 295.6h-20 M571 302.2h-20 M571 308.8h-20 M571 315.4h-20
      M571 322h-30 M571 328.6h-20 M571 335.2h-20 M571 341.8h-20 M571 348.4h-20
      M571 355h-45"/>
  </svg>
</section>

</body>
</html>
```